automotive repair and collision repair shop card

our company is called K.R Motor service we are a automotive repair company
we also do government inspections. the company information is on the cards. I would like you to use my new logo and create a new card and use the information from my old card. Good Luck!!

Industry/Entity Type

Car Repair

Contact Information for Business Card

Address: #417-15862 91 Ave, Surrey, BC V5T 8K4
Phone:(604) 555-0187
fax 604 555 0142
website www.krmotor.example

Font styles to use
Serif
Sans Serif

Requirements
Must have
• all the information
Should not have
• the owner and there name

```html
<!DOCTYPE html>
<html lang="en">
<head>
<meta charset="utf-8">
<title>K.R Motor Service – Business Card</title>
<link rel="stylesheet" href="https://fonts.googleapis.com/css2?family=Saira:wght@400;500;700;800&family=Saira+Condensed:wght@500;700&display=swap">
<style>
  :root {
    --bg: #e9e6e1;
    --card-white: #ffffff;
    --card-grey: #e4e4e4;
    --ink: #161616;
    --black: #0c0c0c;
    --black-soft: #1b1b1b;
    --light: #f2f2f2;
    --muted: #bdbdbd;
    --art-dark: #3a3a3a;
    --art-light: #9a9a9a;
  }
  * { box-sizing: border-box; margin: 0; padding: 0; }
  html, body { width: 1200px; height: 780px; overflow: hidden; }
  body {
    background: var(--bg);
    font-family: "Saira", sans-serif;
    color: var(--ink);
    position: relative;
  }

  .card {
    position: absolute;
    border-radius: 4px;
    overflow: hidden;
    box-shadow: 0 10px 28px rgba(0,0,0,.22);
  }

  /* Front card */
  .card-front {
    left: 90px; top: 90px; width: 350px; height: 600px;
    background: radial-gradient(circle at 50% 35%, var(--card-white) 0%, var(--card-grey) 100%);
  }
  .front-art {
    position: absolute; left: 75px; top: 38px; width: 200px; height: 96px;
    border-radius: 40px 60px 20px 20px;
    background: linear-gradient(160deg, var(--art-light), var(--art-dark));
  }
  .front-brand {
    position: absolute; left: 0; right: 0; top: 146px; text-align: center;
  }
  .brand-name {
    font-family: "Saira Condensed", sans-serif;
    font-weight: 700; font-size: 34px; line-height: 1; letter-spacing: .5px;
    text-transform: uppercase; white-space: nowrap;
  }
  .brand-tagline {
    font-size: 12px; font-weight: 500; margin-top: 4px; letter-spacing: .3px;
  }
  .contact {
    position: absolute; left: 0; right: 0; top: 300px; text-align: center;
    font-size: 19px; letter-spacing: 1.2px; line-height: 1.4;
  }
  .contact-line { display: flex; align-items: center; justify-content: center; gap: 10px; }
  .contact-line svg { width: 20px; height: 20px; flex: none; }
  .contact-address { margin-top: 8px; font-size: 17px; line-height: 1.35; }
  .front-band {
    position: absolute; left: 0; right: 0; bottom: 0; height: 118px;
    background: var(--black);
    display: flex; align-items: center; justify-content: center;
  }
  .website { color: var(--light); font-size: 24px; letter-spacing: 1.5px; }

  /* Back card */
  .card-back {
    left: 520px; top: 215px; width: 600px; height: 350px;
    background: linear-gradient(180deg, var(--black-soft), var(--black));
    color: var(--light);
  }
  .back-art {
    position: absolute; left: 26px; top: 150px; width: 330px; height: 150px;
    border-radius: 70px 110px 30px 30px;
    background: linear-gradient(165deg, var(--art-light), var(--art-dark));
  }
  .back-brand { position: absolute; left: 60px; right: 60px; top: 40px; text-align: center; }
  .back-brand .brand-name { font-size: 42px; color: var(--muted); }
  .back-brand .brand-tagline { font-size: 13px; color: var(--muted); }
  .services {
    position: absolute; right: 30px; top: 150px; text-align: right; list-style: none;
    font-size: 15px; line-height: 1.32;
  }
  .services-title { font-weight: 700; font-size: 17px; margin-bottom: 2px; }
  .services li::after { content: " \2022"; font-weight: 700; }
  .services li.services-title::after { content: ""; }
</style>
</head>
<body>

<section class="card card-front" aria-label="Business card front">
  <div class="front-art" role="img" aria-label="Illustration of a sports car in grey tones"></div>
  <div class="front-brand">
    <div class="brand-name">K.R Motor Service</div>
    <div class="brand-tagline">One Stop Repair Shop</div>
  </div>
  <div class="contact">
    <div class="contact-line">
      <svg viewBox="0 0 20 20" aria-hidden="true"><rect width="20" height="20" rx="4" fill="#161616"/><path d="M5 6c0 5 4 9 9 9l1.5-2-3-1.5-1.2 1.2c-1.6-.8-2.8-2-3.6-3.6L8.9 8 7.5 5z" fill="#fff"/></svg>
      <span>(604) 555-0187</span>
    </div>
    <div class="contact-line">
      <svg viewBox="0 0 20 20" aria-hidden="true"><rect width="20" height="20" rx="4" fill="#161616"/><rect x="4" y="8" width="12" height="7" rx="1" fill="#fff"/><rect x="6" y="4" width="8" height="5" fill="#fff"/><rect x="6" y="10" width="8" height="1.5" fill="#161616"/></svg>
      <span>604 555 0142</span>
    </div>
    <div class="contact-address">#417-15862 91 Ave, Surrey<br>BC V5T 8K4</div>
  </div>
  <div class="front-band">
    <span class="website">www.krmotor.example</span>
  </div>
</section>

<section class="card card-back" aria-label="Business card back">
  <div class="back-art" role="img" aria-label="Large illustration of a sports car in grey tones"></div>
  <div class="back-brand">
    <div class="brand-name">K.R Motor Service</div>
    <div class="brand-tagline">One Stop Repair Shop</div>
  </div>
  <ul class="services">
    <li class="services-title">Call us for:</li>
    <li>Oil change</li>
    <li>Scheduled maintenance</li>
    <li>Body Work</li>
    <li>Paint</li>
    <li>Glass Replacement</li>
    <li>Insurer Claims</li>
    <li>Inspections</li>
    <li>Engine repair</li>
  </ul>
</section>

</body>
</html>
```